Lattiro.com home page upgrade. Strong existing assets.

We are looking to redesign our homepage. We need to communicate three large concepts.

1) Software-as-a-Service for connected electronic device management
2) Mesh-Networking-as-a-Service allows local devices to talk together easily
3) We have 3 pieces of hardware:
A) K7 Beetle
B) K7 Moth
C) K7 Grasshopper

We will keep the color scheme, although we would like the general feel to be lighter than our current page at http://lattiro.com

See the word doc for more details.

Closing soon! Get in last designs! 

Industry/Entity Type

Electronic

Requirements
Nice to have
• large images, modern design

```html
<!DOCTYPE html>
<html lang="en">
<head>
<meta charset="utf-8">
<title>Lattiro — Software as a Service</title>
<link rel="stylesheet" href="https://fonts.googleapis.com/css2?family=Roboto:wght@400;500;700;900&display=swap">
<style>
  :root {
    --brown: #45262d;
    --brown-ink: #4a2a33;
    --orange: #f0892f;
    --orange-dark: #e07a22;
    --icon-grey: #b8a7a9;
    --text: #444;
    --white: #fff;
  }
  * { margin: 0; padding: 0; box-sizing: border-box; }
  html, body { width: 1120px; height: 1200px; overflow: hidden; }
  body { position: relative; background: var(--white); font-family: "Roboto", Arial, sans-serif; color: var(--text); }

  .site-header { position: absolute; top: 0; left: 0; width: 1120px; height: 84px; background: var(--white); }
  .brand { position: absolute; left: 163px; top: 22px; font-size: 40px; font-weight: 900; color: var(--brown); letter-spacing: -1px; line-height: 1; }
  .main-nav { position: absolute; left: 395px; top: 36px; display: flex; gap: 13px; }
  .main-nav a { font-size: 13.5px; color: #333; text-decoration: none; }

  .hero { position: absolute; top: 84px; left: 0; width: 1120px; height: 570px;
    background: linear-gradient(180deg, #8c6a76 0%, #a57c7c 35%, #c98a6d 62%, #7a5a5c 100%); }
  .hero-title { position: absolute; top: 78px; width: 100%; text-align: center; color: var(--white); font-size: 66px; font-weight: 900; letter-spacing: -2px; line-height: 1; }
  .hero-sub { position: absolute; top: 148px; width: 100%; text-align: center; color: var(--brown-ink); font-size: 28px; font-weight: 700; }
  .hero-devices { position: absolute; left: 232px; top: 218px; width: 644px; height: 370px; border-radius: 10px 10px 4px 4px;
    background: radial-gradient(ellipse at 45% 45%, #f2c04a 0%, #c98a1e 55%, #6b4a22 100%); }
  .slide-arrow { position: absolute; top: 260px; width: 32px; height: 32px; }
  .slide-arrow.prev { left: 28px; }
  .slide-arrow.next { left: 1059px; }

  .cta-band { position: absolute; top: 654px; left: 0; width: 1120px; height: 122px; background: var(--orange); }
  .cta-text { position: absolute; top: 46px; width: 100%; text-align: center; font-size: 31px; font-weight: 900; letter-spacing: -1px; }
  .cta-text .ask { color: var(--white); }
  .cta-text .link { color: var(--brown-ink); }
  .cta-text .rest { color: #2a1a1c; }

  .audience { position: absolute; top: 828px; width: 240px; margin-left: -120px; text-align: center; }
  .audience svg { display: block; margin: 0 auto; height: 88px; }
  .audience h2 { margin-top: 32px; font-size: 16.5px; font-weight: 500; color: var(--orange); line-height: 19px; }
  .audience p { margin-top: 14px; font-size: 13px; line-height: 19px; color: var(--text); }
  .btn { display: block; width: 134px; height: 39px; margin: 22px auto 0; line-height: 39px;
    background: linear-gradient(180deg, #f59a45, var(--orange-dark)); border: 1px solid #d9701c;
    color: var(--white); font-size: 13.5px; font-weight: 700; text-decoration: none; text-transform: uppercase; }

  .site-footer { position: absolute; top: 1152px; left: 0; width: 1120px; height: 48px; background: var(--brown); }
  .footer-links { position: absolute; left: 163px; top: 17px; font-size: 11.5px; color: var(--orange); }
  .footer-links a { color: var(--orange); text-decoration: none; }
  .copyright { position: absolute; right: 165px; top: 18px; font-size: 10px; color: var(--white); font-weight: 500; }
</style>
</head>
<body>
  <header class="site-header">
    <div class="brand">Lattiro</div>
    <nav class="main-nav">
      <a href="#">Manufacturers</a><a href="#">Technology Integrators</a><a href="#">Enterprise Plans</a><a href="#">K7 Devices</a><a href="#">About Us</a><a href="#">Contact Us</a>
    </nav>
  </header>

  <section class="hero">
    <h1 class="hero-title">Software as a Service</h1>
    <p class="hero-sub">Lattiro Solutions require no IT infrastructure or overhead</p>
    <div class="hero-devices" role="img" aria-label="Laptop and smartphone showing the product dashboard on a golden background"></div>
    <svg class="slide-arrow prev" viewBox="0 0 32 32"><circle cx="16" cy="16" r="16" fill="#000"/><path d="M18 10l-6 6 6 6" stroke="#fff" stroke-width="3" fill="none"/></svg>
    <svg class="slide-arrow next" viewBox="0 0 32 32"><circle cx="16" cy="16" r="16" fill="#000"/><path d="M14 10l6 6-6 6" stroke="#fff" stroke-width="3" fill="none"/></svg>
  </section>

  <section class="cta-band">
    <p class="cta-text"><span class="ask">Unless you want it to?</span> <span class="link">Click here</span> <span class="rest">for Enterprise Plans.</span></p>
  </section>

  <section class="audience" style="left:291px">
    <svg viewBox="0 0 86 88"><path d="M0 88V4q0-4 4-4h10v40l18-12v12l18-12v12l18-12v12l18-12v60z" fill="var(--icon-grey)"/><rect x="22" y="58" width="9" height="9" rx="2" fill="#fff"/><rect x="45" y="58" width="9" height="9" rx="2" fill="#fff"/><rect x="67" y="58" width="9" height="9" rx="2" fill="#fff"/></svg>
    <h2>Lattiro<br>For OEM’s</h2>
    <p>New Revenue! Add a Web and Mobile M2M Product-Line with Lattiro</p>
    <a class="btn" href="#">Learn More</a>
  </section>

  <section class="audience" style="left:560px">
    <svg viewBox="0 0 88 88"><g fill="var(--icon-grey)"><rect x="14" y="14" width="60" height="60" rx="8"/><rect x="22" y="0" width="10" height="88" rx="3"/><rect x="39" y="0" width="10" height="88" rx="3"/><rect x="56" y="0" width="10" height="88" rx="3"/><rect x="0" y="22" width="88" height="10" rx="3"/><rect x="0" y="39" width="88" height="10" rx="3"/><rect x="0" y="56" width="88" height="10" rx="3"/></g><rect x="26" y="26" width="36" height="36" rx="5" fill="#fff"/><rect x="30" y="30" width="28" height="28" rx="3" fill="var(--icon-grey)"/></svg>
    <h2>Lattiro<br>For Technology Integrators</h2>
    <p>Enhance Your Service Offering with Connected Devices!</p>
    <a class="btn" href="#">Learn More</a>
  </section>

  <section class="audience" style="left:829px">
    <svg viewBox="0 0 94 88"><path d="M0 88v-8h11V0h72v80h11v8H54V72H40v16z" fill="var(--icon-grey)"/><g fill="#fff"><rect x="30" y="15" width="11" height="11" rx="2"/><rect x="52" y="15" width="11" height="11" rx="2"/><rect x="30" y="33" width="11" height="11" rx="2"/><rect x="52" y="33" width="11" height="11" rx="2"/><rect x="30" y="51" width="11" height="11" rx="2"/><rect x="52" y="51" width="11" height="11" rx="2"/></g></svg>
    <h2>Lattiro Enterprise Plans<br>For Companies</h2>
    <p>Quickly get a solution running that ties to your back office</p>
    <a class="btn" href="#">Learn More</a>
  </section>

  <footer class="site-footer">
    <div class="footer-links"><a href="#">Home</a> | <a href="#">Manufacturers</a> | <a href="#">Technology Integrators</a> | <a href="#">Enterprise Plans</a> | <a href="#">K7 Devices</a> | <a href="#">About Us</a> | <a href="#">Contact Us</a></div>
    <div class="copyright">Copyright © 2013 lattiro. all rights reserved</div>
  </footer>
</body>
</html>
```